FE-N-DRA corporate branding Powerpoint template*

We are a IT / tech company focussed on no nonsense services for our customers. Our main colors are blue and Orange as seen in the attached logo. Our catchphrase is Simply Fendra. We will use this template for corporate presentations at customers and potential projects.Please make sure the powerpoint does not have any art in there as the standard computers or whatsoever. We want a sleek clean design with our logo and both our colors in a main role.

Target Market(s)

Our existing customers and new customers

Industry/Entity Type

It Company

Colors

Requirements
Must have
• Different slides for different scenarios.
• Look and feel across the entire template
Nice to have
• Enough space to have our own bullet points
Should not have
• To overcrowded slides. Too loud design.

```html
<!DOCTYPE html>
<html lang="en">
<head>
<meta charset="utf-8">
<title>FE-N-DRA Presentation Template Overview</title>
<link href="https://fonts.googleapis.com/css2?family=Roboto:wght@400;500;700;900&display=swap" rel="stylesheet">
<style>
:root{
  --blue:#1e4b91;
  --blue-dark:#163a72;
  --orange:#f07020;
  --grey:#eeeeee;
  --grey-mid:#9a9a9a;
  --ink:#151515;
  --text:#4a4a4a;
  --canvas:#cbcbcb;
}
html,body{margin:0;padding:0;overflow:hidden}
body{width:1200px;height:1198px;background:var(--canvas);position:relative;font-family:'Roboto',Arial,sans-serif}
.defs{position:absolute;width:0;height:0}
.slide{position:absolute;width:277px;height:155px;background:#fff;box-shadow:0 2px 5px rgba(0,0,0,.28);overflow:hidden}
.slide svg{display:block;width:277px;height:155px}
.c1{left:27px}.c2{left:314px}.c3{left:600px}.c4{left:886px}
.r1{top:30px}.r2{top:194px}.r3{top:358px}.r4{top:522px}.r5{top:686px}.r6{top:850px}.r7{top:1014px}
.b1{left:166px}.b2{left:452px}.b3{left:738px}
text{font-family:'Roboto',Arial,sans-serif}
.title{font-size:11px;font-weight:700;fill:var(--ink);text-anchor:middle}
.tx{font-size:2.5px;fill:var(--text)}
.txc{font-size:2.5px;fill:var(--text);text-anchor:middle}
.head{font-size:3.3px;font-weight:700;fill:var(--blue)}
.headc{font-size:3.3px;font-weight:700;fill:var(--ink);text-anchor:middle}
.wordmark{font-weight:900;fill:var(--blue);text-anchor:middle;letter-spacing:.5px}
.tagline{fill:#333;text-anchor:middle;letter-spacing:2.6px}
.white{fill:#fff}
.orange{fill:var(--orange)}
.blue{fill:var(--blue)}
.ico{fill:none;stroke:#fff;stroke-width:1;stroke-linecap:round;stroke-linejoin:round}
</style>
</head>
<body>

<svg class="defs" aria-hidden="true">
  <defs>
    <g id="foot">
      <text x="4" y="151" style="font-size:3.4px;font-weight:900;fill:var(--blue)">FE·N·DRA</text>
      <rect x="24" y="148.5" width="244" height="2" fill="var(--blue)"/>
      <circle cx="262" cy="149.5" r="3" fill="#fff" stroke="#ccc" stroke-width=".4"/>
    </g>
    <rect id="tab" x="126.5" y="0" width="24" height="1.6" fill="var(--orange)"/>
    <text id="para" class="tx">
      <tspan x="0" dy="0">Lorem ipsum dolor sit amet, consectetur adipiscing elit, sed do</tspan>
      <tspan x="0" dy="3.6">eiusmod tempor incididunt ut labore et dolore magna aliqua. Lorem</tspan>
      <tspan x="0" dy="3.6">ipsum dolor sit amet, consectetur adipiscing elit, sed do eiusmod</tspan>
      <tspan x="0" dy="3.6">tempor incididunt ut labore et dolore magna aliqua. Ut enim ad</tspan>
      <tspan x="0" dy="3.6">minim veniam, quis nostrud exercitation ullamco laboris nisi ut</tspan>
      <tspan x="0" dy="3.6">aliquip ex ea commodo consequat, sed do eiusmod tempor.</tspan>
    </text>
    <text id="short" class="tx">
      <tspan x="0" dy="0">Lorem ipsum dolor sit amet, consectetur</tspan>
      <tspan x="0" dy="3.4">adipiscing elit, sed do eiusmod tempor</tspan>
      <tspan x="0" dy="3.4">incididunt ut labore et dolore magna.</tspan>
    </text>
    <text id="bul" class="tx">
      <tspan x="0" dy="0">Nulla varius vehicula augue, id placerat nisl luctus a. Suspendisse</tspan>
      <tspan x="0" dy="3.4">tellus, imperdiet id turpis in, gravida fermentum sem. Integer</tspan>
      <tspan x="0" dy="3.4">pharetra dui a congue. Vivamus.</tspan>
    </text>
    <text id="col" class="tx">
      <tspan x="0" dy="0">Lorem ipsum dolor sit amet,</tspan>
      <tspan x="0" dy="3.6">consectetur adipiscing elit, sed do</tspan>
      <tspan x="0" dy="3.6">eiusmod tempor incididunt ut labore et</tspan>
      <tspan x="0" dy="3.6">dolore magna aliqua. Lorem ipsum</tspan>
      <tspan x="0" dy="3.6">dolor sit amet, consectetur adipiscing</tspan>
      <tspan x="0" dy="3.6">elit, sed do eiusmod tempor incididunt</tspan>
      <tspan x="0" dy="3.6">ut labore et dolore magna aliqua.</tspan>
      <tspan x="0" dy="3.6">Lorem ipsum dolor sit amet,</tspan>
      <tspan x="0" dy="3.6">consectetur adipiscing elit, sed do</tspan>
      <tspan x="0" dy="3.6">eiusmod tempor incididunt ut labore et</tspan>
      <tspan x="0" dy="3.6">dolore magna aliqua.</tspan>
    </text>
    <linearGradient id="gBlue" x1="0" y1="0" x2="1" y2="1">
      <stop offset="0" stop-color="#2a5aa6"/><stop offset="1" stop-color="#173c78"/>
    </linearGradient>
    <linearGradient id="gOrange" x1="0" y1="0" x2="1" y2="1">
      <stop offset="0" stop-color="#f58a3c"/><stop offset="1" stop-color="#e2661a"/>
    </linearGradient>
    <linearGradient id="gPhoto" x1="0" y1="0" x2="1" y2="1">
      <stop offset="0" stop-color="#2f4a5c"/><stop offset=".5" stop-color="#8ab0c4"/><stop offset="1" stop-color="#1d2d3a"/>
    </linearGradient>
  </defs>
</svg>

<!-- Row 1: title slides -->
<section class="slide c1 r1">
  <svg viewBox="0 0 277 155">
    <text class="wordmark" x="138.5" y="70" style="font-size:26px">FE·N·DRA</text>
    <text class="tagline" x="138.5" y="83" style="font-size:6px">SIMPLY FENDRA</text>
    <rect y="127" width="277" height="28" fill="var(--blue)"/>
    <text x="138.5" y="140" text-anchor="middle" style="font-size:9.5px;font-weight:700" class="white">PRESENTATION TITLE</text>
    <text x="138.5" y="150" text-anchor="middle" style="font-size:6.5px" class="white">Sub title goes here</text>
  </svg>
</section>

<section class="slide c2 r1">
  <svg viewBox="0 0 277 155">
    <path d="M12 10H178L188 19H267V146H95L85 137H12Z" fill="var(--blue)"/>
    <text class="wordmark" x="140" y="50" style="font-size:17px;fill:#fff">FE·N·DRA</text>
    <text class="tagline" x="140" y="58" style="font-size:4.5px;fill:#fff">SIMPLY FENDRA</text>
    <text x="140" y="92" text-anchor="middle" class="orange" style="font-size:13px;font-weight:700">PRESENTATION TITLE</text>
    <text x="140" y="102" text-anchor="middle" class="white" style="font-size:7px;font-weight:700">Sub title goes here</text>
  </svg>
</section>

<section class="slide c3 r1">
  <svg viewBox="0 0 277 155">
    <path d="M12 10H178L188 19H267V146H95L85 137H12Z" fill="var(--blue)"/>
    <rect x="16" y="22" width="110" height="112" rx="4" fill="url(#gOrange)" role="img" aria-label="Orange brand visual with tablet imagery"/>
    <text x="132" y="81" class="orange" style="font-size:9.5px;font-weight:700">PRESENTATION TITLE</text>
    <text x="132" y="88" class="white" style="font-size:5.5px;font-weight:700">Sub title goes here</text>
  </svg>
</section>

<section class="slide c4 r1">
  <svg viewBox="0 0 277 155">
    <rect width="277" height="155" fill="url(#gBlue)" role="img" aria-label="Blue-tinted photo of a person reviewing charts"/>
    <line x1="138.5" y1="0" x2="138.5" y2="34" stroke="#fff" stroke-width=".5"/>
    <text class="wordmark" x="138.5" y="62" style="font-size:25px;fill:#fff">FE·N·DRA</text>
    <text class="tagline" x="138.5" y="75" style="font-size:6px;fill:#fff">SIMPLY FENDRA</text>
    <line x1="138.5" y1="80" x2="138.5" y2="112" stroke="#fff" stroke-width=".5"/>
    <line x1="30" y1="112" x2="247" y2="112" stroke="#fff" stroke-width=".5"/>
    <text x="138.5" y="124" text-anchor="middle" class="white" style="font-size:9.5px;font-weight:700">PRESENTATION TITLE</text>
    <text x="138.5" y="134" text-anchor="middle" class="white" style="font-size:6.5px">Sub title goes here</text>
    <line x1="30" y1="143" x2="247" y2="143" stroke="#fff" stroke-width=".5"/>
    <rect x="126.5" y="153" width="24" height="2" fill="var(--orange)"/>
  </svg>
</section>

<!-- Row 2 -->
<section class="slide c1 r2">
  <svg viewBox="0 0 277 155">
    <text x="50" y="72" text-anchor="middle" class="blue" style="font-size:12.5px;font-weight:500">Table of</text>
    <text x="50" y="89" text-anchor="middle" class="blue" style="font-size:12.5px;font-weight:500">contents</text>
    <rect x="99" width="17" height="155" fill="var(--blue)"/>
    <g>
      <text x="107.5" y="25" text-anchor="middle" class="white" style="font-size:10px;font-weight:700">01</text>
      <text x="121" y="22" style="font-size:7.5px;font-weight:700">Contents</text>
      <text x="121" y="27" class="tx">Get a modern presentation that is beautifully designed. I hope</text>
      <text x="121" y="30.5" class="tx">and I believe that this template will save your time.</text>
      <text x="107.5" y="50" text-anchor="middle" class="white" style="font-size:10px;font-weight:700">02</text>
      <text x="121" y="47" style="font-size:7.5px;font-weight:700">Contents</text>
      <text x="121" y="52" class="tx">Get a modern presentation that is beautifully designed. I hope</text>
      <text x="121" y="55.5" class="tx">and I believe that this template will save your time.</text>
      <text x="107.5" y="75" text-anchor="middle" class="white" style="font-size:10px;font-weight:700">03</text>
      <text x="121" y="72" style="font-size:7.5px;font-weight:700">Contents</text>
      <text x="121" y="77" class="tx">Get a modern presentation that is beautifully designed. I hope</text>
      <text x="121" y="80.5" class="tx">and I believe that this template will save your time.</text>
      <text x="107.5" y="99" text-anchor="middle" class="white" style="font-size:10px;font-weight:700">04</text>
      <text x="121" y="96" style="font-size:7.5px;font-weight:700">Contents</text>
      <text x="121" y="101" class="tx">Get a modern presentation that is beautifully designed. I hope</text>
      <text x="121" y="104.5" class="tx">and I believe that this template will save your time.</text>
      <text x="107.5" y="124" text-anchor="middle" class="white" style="font-size:10px;font-weight:700">05</text>
      <text x="121" y="121" style="font-size:7.5px;font-weight:700">Contents</text>
      <text x="121" y="126" class="tx">Get a modern presentation that is beautifully designed. I hope and</text>
      <text x="121" y="129.5" class="tx">I believe that this template will save your time.</text>
    </g>
  </svg>
</section>

<section class="slide c2 r2">
  <svg viewBox="0 0 277 155">
    <use href="#tab"/>
    <text class="title" x="138.5" y="28">Lorem ipsum dolor sit amet</text>
    <polygon points="22,51 261,51 253,83 14,83" fill="var(--blue)"/>
    <text x="138" y="60" text-anchor="middle" class="white" style="font-size:3.6px">Every once in a while, a new technology, an old problem, and a big idea turn into an</text>
    <text x="138" y="65" text-anchor="middle" class="white" style="font-size:3.6px">innovation.</text>
    <text x="138" y="73" text-anchor="middle" class="white" style="font-size:3.6px;font-weight:700">Dana Korven</text>
    <circle cx="70" cy="88" r="9" fill="var(--orange)" stroke="#fff" stroke-width="1.5"/>
    <circle cx="70" cy="88" r="3" class="ico"/>
    <circle cx="195" cy="88" r="9" fill="var(--orange)" stroke="#fff" stroke-width="1.5"/>
    <path d="M195 84.5a2.8 2.8 0 0 1 1.6 5v1.5h-3.2v-1.5a2.8 2.8 0 0 1 1.6-5z" class="ico"/>
    <use href="#short" x="27" y="112"/>
    <use href="#short" x="152" y="112"/>
    <use href="#foot"/>
  </svg>
</section>

<section class="slide c3 r2">
  <svg viewBox="0 0 277 155">
    <use href="#tab"/>
    <text class="title" x="138.5" y="21">Lorem ipsum dolor sit amet</text>
    <text x="138.5" y="30" class="txc">Lorem ipsum dolor sit amet, consectetur adipiscing elit, sed do eiusmod</text>
    <text x="138.5" y="34" class="txc">tempor incididunt ut labore et dolore magna aliqua</text>
    <rect y="42" width="277" height="98" fill="#efefef"/>
    <circle cx="51" cy="63" r="9" fill="var(--blue)"/>
    <path d="M47 67l4-8 4 8M48.5 64h5" class="ico"/>
    <circle cx="138" cy="63" r="9" fill="var(--blue)"/>
    <circle cx="138" cy="60.5" r="2" class="ico"/><path d="M134.5 67a3.5 3 0 0 1 7 0" class="ico"/>
    <circle cx="227" cy="63" r="9" fill="var(--blue)"/>
    <path d="M223 61.5a4 3.2 0 1 1 2 2.8l-2 1.5z" class="ico"/>
    <text x="51" y="81" text-anchor="middle" class="blue" style="font-size:2.9px;font-weight:700">ROAD TO THE CLOUD</text>
    <text x="138" y="81" text-anchor="middle" class="blue" style="font-size:2.9px;font-weight:700">EMPOWER YOUR USERS</text>
    <text x="227" y="81" text-anchor="middle" class="blue" style="font-size:2.9px;font-weight:700">FE-N-DRA CONNECTED CARE</text>
    <use href="#short" x="28" y="87"/>
    <use href="#short" x="115" y="87"/>
    <use href="#short" x="204" y="87"/>
    <use href="#foot"/>
  </svg>
</section>

<section class="slide c4 r2">
  <svg viewBox="0 0 277 155">
    <use href="#tab"/>
    <text class="title" x="138.5" y="22">An executive summary</text>
    <use href="#para" x="28" y="45"/>
    <use href="#para" x="28" y="72"/>
    <use href="#para" x="158" y="45"/>
    <use href="#para" x="158" y="72"/>
    <use href="#foot"/>
  </svg>
</section>

<!-- Row 3 -->
<section class="slide c1 r3">
  <svg viewBox="0 0 277 155">
    <use href="#tab"/>
    <text class="title" x="138.5" y="22">3 column page</text>
    <text x="18" y="44" class="head">LOREM IPSUM DOLOR SIT</text>
    <text x="105" y="44" class="head">LOREM IPSUM DOLOR SIT</text>
    <text x="193" y="44" class="head">LOREM IPSUM DOLOR SIT</text>
    <use href="#col" x="18" y="52"/>
    <use href="#col" x="105" y="52"/>
    <use href="#col" x="193" y="52"/>
    <use href="#foot"/>
  </svg>
</section>

<section class="slide c2 r3">
  <svg viewBox="0 0 277 155">
    <use href="#tab"/>
    <text class="title" x="138.5" y="22">Bulleted List Text Sample</text>
    <g style="font-size:3px;font-weight:700">
      <text x="17" y="44">▸ Your first Title goes here:</text>
      <text x="148" y="44">▸ Your first Title goes here:</text>
      <text x="17" y="76">▸ Your second Title goes here:</text>
      <text x="148" y="76">▸ Your second Title goes here:</text>
      <text x="17" y="108">▸ Your third Title goes here:</text>
      <text x="148" y="108">▸ Your third Title goes here:</text>
    </g>
    <use href="#bul" x="17" y="51"/><use href="#bul" x="148" y="51"/>
    <use href="#bul" x="17" y="83"/><use href="#bul" x="148" y="83"/>
    <use href="#bul" x="17" y="115"/><use href="#bul" x="148" y="115"/>
    <use href="#foot"/>
  </svg>
</section>

<section class="slide c3 r3">
  <svg viewBox="0 0 277 155">
    <use href="#tab"/>
    <text class="title" x="138.5" y="22">Your Title Here</text>
    <text class="wordmark" x="138.5" y="90" style="font-size:42px;fill:#e9ecf4">FE·N·DRA</text>
    <text class="tagline" x="138.5" y="106" style="font-size:11px;fill:#eef0f5;letter-spacing:8px">SIMPLY FENDRA</text>
    <use href="#foot"/>
  </svg>
</section>

<section class="slide c4 r3">
  <svg viewBox="0 0 277 155">
    <rect width="172" height="115" fill="url(#gPhoto)" role="img" aria-label="Photo of a modern corridor with light trails"/>
    <rect x="189" y="17" width="47" height="65" rx="6" fill="var(--blue)"/>
    <text x="212.5" y="40" text-anchor="middle" class="white" style="font-size:7px;font-weight:500">Lorem</text>
    <text x="212.5" y="50" text-anchor="middle" class="white" style="font-size:7px;font-weight:500">ipsum dolor</text>
    <text x="212.5" y="60" text-anchor="middle" class="white" style="font-size:7px;font-weight:500">sit amet</text>
    <rect x="64" y="70" width="176" height="74" rx="5" fill="#fff" stroke="#e4e4e4" stroke-width=".4"/>
    <g>
      <circle cx="77" cy="81" r="3" fill="var(--blue)"/><circle cx="77" cy="91.5" r="3" fill="var(--blue)"/>
      <circle cx="77" cy="102" r="3" fill="var(--blue)"/><circle cx="77" cy="112.5" r="3" fill="var(--blue)"/>
      <circle cx="77" cy="123" r="3" fill="var(--blue)"/><circle cx="77" cy="133.5" r="3" fill="var(--blue)"/>
      <path d="M75.5 81l1 1 2-2M75.5 91.5l1 1 2-2M75.5 102l1 1 2-2M75.5 112.5l1 1 2-2M75.5 123l1 1 2-2M75.5 133.5l1 1 2-2" fill="none" stroke="#fff" stroke-width=".6"/>
      <text x="85" y="82" class="tx">Lorem ipsum dolor sit amet, consectetur adipiscing elit</text>
      <text x="85" y="92.5" class="tx">Lorem ipsum dolor sit amet, consectetur adipiscing elit</text>
      <text x="85" y="103" class="tx">Lorem ipsum dolor sit amet, consectetur amet, consectetur adipiscing elit</text>
      <text x="85" y="113.5" class="tx">Lorem ipsum dolor sit amet, consectetur amet, consectetur adipiscing elit</text>
      <text x="85" y="124" class="tx">Lorem ipsum dolor sit amet, consectetur lorem ipsum dolor sit amet, consectetur amet</text>
      <text x="85" y="134.5" class="tx">Lorem ipsum dolor sit amet, consectetur adipiscing elit</text>
    </g>
    <use href="#foot"/>
  </svg>
</section>

<!-- Row 4 -->
<section class="slide c1 r4">
  <svg viewBox="0 0 277 155">
    <use href="#tab"/>
    <text class="title" x="138.5" y="22">Lorem ipsum dolor sit amet</text>
    <text class="wordmark" x="45" y="85" style="font-size:16px">FE·N·DRA</text>
    <text class="tagline" x="45" y="92" style="font-size:4px">SIMPLY FENDRA</text>
    <path d="M148 48H99V117H148M99 82H148" fill="none" stroke="#bbb" stroke-width=".5"/>
    <rect x="143" y="42" width="52" height="6" rx="3" fill="var(--blue)"/>
    <text x="152" y="46.2" class="white" style="font-size:3.3px">Your Title</text>
    <use href="#short" x="143" y="53"/>
    <rect x="143" y="76" width="52" height="6" rx="3" fill="var(--blue)"/>
    <text x="152" y="80.2" class="white" style="font-size:3.3px">Your Title</text>
    <use href="#short" x="143" y="87"/>
    <rect x="143" y="111" width="52" height="6" rx="3" fill="var(--blue)"/>
    <text x="152" y="115.2" class="white" style="font-size:3.3px">Your Title</text>
    <use href="#short" x="143" y="122"/>
    <use href="#foot"/>
  </svg>
</section>

<section class="slide c2 r4">
  <svg viewBox="0 0 277 155">
    <use href="#tab"/>
    <text class="title" x="138.5" y="22">Services</text>
    <g fill="#ececec">
      <rect x="17" y="42" width="79" height="38"/><rect x="99" y="42" width="79" height="38"/><rect x="181" y="42" width="79" height="38"/>
      <rect x="17" y="99" width="79" height="38"/><rect x="99" y="99" width="79" height="38"/><rect x="181" y="99" width="79" height="38"/>
    </g>
    <g fill="var(--blue)" stroke="#fff" stroke-width="1.2">
      <circle cx="56.5" cy="41" r="8"/><circle cx="138.5" cy="41" r="8"/><circle cx="220.5" cy="41" r="8"/>
      <circle cx="56.5" cy="98" r="8"/><circle cx="138.5" cy="98" r="8"/><circle cx="220.5" cy="98" r="8"/>
    </g>
    <path d="M53.5 44V38M56 44V39.5M58.5 44V37.5" class="ico"/>
    <circle cx="138.5" cy="41" r="2.6" class="ico"/>
    <path d="M220.5 37.5a2.5 2.5 0 0 1 1.4 4.5v1.5h-2.8v-1.5a2.5 2.5 0 0 1 1.4-4.5z" class="ico"/>
    <circle cx="55.8" cy="97.3" r="2.2" class="ico"/><path d="M57.5 99l2 2" class="ico"/>
    <path d="M135 95.5h7v4.5h-7zM134 101.5h9" class="ico"/>
    <rect x="218.5" y="94.5" width="4" height="7" rx=".6" class="ico"/>
    <g class="headc" style="font-size:3.6px">
      <text x="56.5" y="60">Lorem ipsum dolor</text><text x="138.5" y="60">Lorem ipsum dolor</text><text x="220.5" y="60">Lorem ipsum dolor</text>
      <text x="56.5" y="117">Lorem ipsum dolor</text><text x="138.5" y="117">Lorem ipsum dolor</text><text x="220.5" y="117">Lorem ipsum dolor</text>
    </g>
    <g class="txc">
      <text x="56.5" y="66">Lorem ipsum dolor sit amet, consectetur</text><text x="56.5" y="69.5">adipiscing elit, sed do eiusmod tempor</text>
      <text x="138.5" y="66">Lorem ipsum dolor sit amet, consectetur</text><text x="138.5" y="69.5">adipiscing elit, sed do eiusmod tempor</text>
      <text x="220.5" y="66">Lorem ipsum dolor sit amet, consectetur</text><text x="220.5" y="69.5">adipiscing elit, sed do eiusmod tempor</text>
      <text x="56.5" y="123">Lorem ipsum dolor sit amet, consectetur</text><text x="56.5" y="126.5">adipiscing elit, sed do eiusmod tempor</text>
      <text x="138.5" y="123">Lorem ipsum dolor sit amet, consectetur</text><text x="138.5" y="126.5">adipiscing elit, sed do eiusmod tempor</text>
      <text x="220.5" y="123">Lorem ipsum dolor sit amet, consectetur</text><text x="220.5" y="126.5">adipiscing elit, sed do eiusmod tempor</text>
    </g>
    <use href="#foot"/>
  </svg>
</section>

<section class="slide c3 r4">
  <svg viewBox="0 0 277 155">
    <use href="#tab"/>
    <text class="title" x="138.5" y="22">The Solution</text>
    <text x="138.5" y="28" class="txc" style="fill:#bbb">Lorem ipsum dolor sit amet, consectetur adipiscing elit, sed do eiusmod sit amet</text>
    <g fill="#ececec">
      <rect x="33" y="44" width="92" height="38"/><rect x="164" y="44" width="92" height="38"/>
      <rect x="33" y="90" width="92" height="38"/><rect x="164" y="90" width="92" height="38"/>
    </g>
    <g fill="var(--blue)" stroke="#fff" stroke-width="1.2">
      <circle cx="31" cy="63" r="11"/><circle cx="162" cy="63" r="11"/>
      <circle cx="31" cy="109" r="11"/><circle cx="162" cy="109" r="11"/>
    </g>
    <path d="M27.5 66.5V61M30.5 66.5V59M33.5 66.5V62" class="ico"/>
    <circle cx="162" cy="60" r="2.3" class="ico"/><path d="M158 67a4 3.4 0 0 1 8 0" class="ico"/>
    <path d="M27.5 113l3.5-8 3.5 8M29 110h4" class="ico"/>
    <path d="M157.5 108a4.5 3.6 0 1 1 2.2 3l-2.2 1.6z" class="ico"/>
    <g style="font-size:3.6px;font-weight:700">
      <text x="46" y="53">Lorem ipsum dolor</text><text x="177" y="53">Lorem ipsum dolor</text>
      <text x="46" y="99">Lorem ipsum dolor</text><text x="177" y="99">Lorem ipsum dolor</text>
    </g>
    <use href="#short" x="46" y="59"/><use href="#short" x="177" y="59"/>
    <use href="#short" x="46" y="105"/><use href="#short" x="177" y="105"/>
    <use href="#foot"/>
  </svg>
</section>

<section class="slide c4 r4">
  <svg viewBox="0 0 277 155">
    <use href="#tab"/>
    <text class="title" x="138.5" y="22">Our Process</text>
    <g class="head" style="font-size:3.6px">
      <text x="17" y="36">Step One</text><text x="17" y="59">Step Two</text><text x="17" y="82">Step Three</text>
      <text x="17" y="105">Step Four</text><text x="17" y="128">Step Four</text>
    </g>
    <g class="tx" style="fill:#bbb">
      <text x="17" y="40">This is a sample text. Insert your desired text here this is a</text><text x="17" y="43.5">sample text. Insert your desired text here.</text>
      <text x="17" y="63">This is a sample text. Insert your desired text here this is a</text><text x="17" y="66.5">sample text. Insert your desired text here.</text>
      <text x="17" y="86">This is a sample text. Insert your desired text here this is a</text><text x="17" y="89.5">sample text. Insert your desired text here.</text>
      <text x="17" y="109">This is a sample text. Insert your desired text here this is a</text><text x="17" y="112.5">sample text. Insert your desired text here.</text>
      <text x="17" y="132">This is a sample text. Insert your desired text here this is a</text><text x="17" y="135.5">sample text. Insert your desired text here.</text>
    </g>
    <circle cx="209" cy="46" r="12" fill="var(--blue)"/>
    <circle cx="246" cy="74" r="12" fill="#9b9b9b"/>
    <circle cx="232" cy="118" r="12" fill="var(--orange)"/>
    <circle cx="186" cy="118" r="12" fill="#555"/>
    <circle cx="172" cy="74" r="12" fill="var(--orange)"/>
    <g class="white" text-anchor="middle" style="font-size:3.6px;font-weight:700">
      <text x="209" y="47.2">Step 1</text><text x="246" y="75.2">Step 2</text><text x="232" y="119.2">Step 3</text>
      <text x="186" y="119.2">Step 4</text><text x="172" y="75.2">Step 5</text>
    </g>
    <g fill="var(--orange)">
      <polygon points="188,62 193,57 194,63"/><polygon points="210,118 214,114.5 214,121.5"/>
    </g>
    <g fill="var(--blue)"><polygon points="224,55 230,60 224,61"/></g>
    <g fill="#888"><polygon points="240,92 244,91 241,96"/><polygon points="174,97 178,92 179,98"/></g>
    <text class="wordmark" x="209" y="90" style="font-size:8px">FE·N·DRA</text>
    <text class="tagline" x="209" y="94" style="font-size:2px;letter-spacing:1px">SIMPLY FENDRA</text>
    <use href="#foot"/>
  </svg>
</section>

<!-- Row 5 -->
<section class="slide c1 r5">
  <svg viewBox="0 0 277 155">
    <rect x="0" y="20" width="11" height="108" fill="var(--blue)"/>
    <use href="#para" x="20" y="18"/>
    <use href="#para" x="20" y="40"/>
    <use href="#para" x="20" y="84"/>
    <use href="#para" x="20" y="106"/>
    <rect x="138" width="139" height="155" fill="url(#gBlue)" role="img" aria-label="Blue-toned photo of a futuristic tunnel"/>
    <g class="white" text-anchor="middle" style="font-size:9.5px;font-weight:700">
      <text x="207" y="52">Lorem ipsum</text><text x="207" y="64">consectetur</text>
      <text x="207" y="76">adipiscing elit,</text><text x="207" y="88">eiusmod tempor</text>
      <text x="207" y="100">incididunt</text>
    </g>
    <use href="#foot"/>
  </svg>
</section>

<section class="slide c2 r5">
  <svg viewBox="0 0 277 155">
    <use href="#tab"/>
    <text class="title" x="138.5" y="22">The Market</text>
    <circle cx="62" cy="81" r="42" fill="var(--orange)"/>
    <circle cx="64" cy="96" r="27" fill="#325a9a"/>
    <circle cx="63" cy="110" r="13" fill="#a8a8a8"/>
    <g class="white" text-anchor="middle" style="font-size:7px;font-weight:700">
      <text x="62" y="55">$</text><text x="62" y="79">$</text><text x="63" y="113">$</text>
    </g>
    <g stroke="#999" stroke-width=".4"><line x1="66" y1="52" x2="112" y2="52"/><line x1="70" y1="76" x2="112" y2="76"/><line x1="70" y1="106" x2="112" y2="106"/></g>
    <g style="font-size:8px;fill:#444">
      <text x="114" y="55">999M</text><text x="114" y="79">99M</text><text x="114" y="109">9M</text>
    </g>
    <circle cx="176" cy="53" r="6" fill="var(--orange)"/>
    <circle cx="176" cy="80" r="6" fill="var(--blue)"/>
    <circle cx="176" cy="109" r="6" fill="#bbb"/>
    <path d="M173.5 53l2 2 3.5-3.5M173.5 80l2 2 3.5-3.5M173.5 109l2 2 3.5-3.5" fill="none" stroke="#fff" stroke-width="1"/>
    <g style="font-size:3.2px;font-weight:700">
      <text x="188" y="49">Lorem ipsum dolor</text><text x="188" y="76">Lorem ipsum dolor</text><text x="188" y="105">Lorem ipsum dolor</text>
    </g>
    <g class="tx">
      <text x="188" y="53.5">Lorem ipsum dolor sit amet, consectetur</text><text x="188" y="57">adipiscing elit, sed do eiusmod tempor</text>
      <text x="188" y="80.5">Lorem ipsum dolor sit amet, consectetur</text><text x="188" y="84">adipiscing elit, sed do eiusmod tempor</text>
      <text x="188" y="109.5">Lorem ipsum dolor sit amet, consectetur</text><text x="188" y="113">adipiscing elit, sed do eiusmod tempor</text>
    </g>
    <use href="#foot"/>
  </svg>
</section>

<section class="slide c3 r5">
  <svg viewBox="0 0 277 155">
    <use href="#tab"/>
    <text class="title" x="138.5" y="22">Text content with a graph</text>
    <use href="#para" x="19" y="44"/>
    <use href="#para" x="19" y="66"/>
    <use href="#para" x="19" y="88"/>
    <use href="#para" x="19" y="110"/>
    <text x="138" y="55" style="font-size:19px;fill:#9a9a9a">250K</text>
    <text x="194" y="44" class="tx">Sed ut perspiciatis, unde omnis iste natus</text>
    <text x="194" y="47.5" class="tx">error sit voluptatem accusantium</text>
    <text x="194" y="51" class="tx">doloremque laudantium, totam rem</text>
    <g>
      <rect x="140" y="73" width="65" height="4.5" fill="var(--blue)"/><rect x="205" y="73" width="41" height="4.5" fill="var(--orange)"/>
      <rect x="140" y="87" width="51" height="4.5" fill="var(--blue)"/><rect x="191" y="87" width="26" height="4.5" fill="var(--orange)"/>
      <rect x="140" y="101" width="36" height="4.5" fill="var(--blue)"/><rect x="176" y="101" width="64" height="4.5" fill="var(--orange)"/>
      <rect x="140" y="115" width="62" height="4.5" fill="var(--blue)"/><rect x="202" y="115" width="35" height="4.5" fill="var(--orange)"/>
    </g>
    <line x1="140" y1="126" x2="258" y2="126" stroke="#999" stroke-width=".4"/>
    <g class="txc">
      <text x="140" y="131">0</text><text x="154.5" y="131">1</text><text x="169" y="131">2</text><text x="183.5" y="131">3</text>
      <text x="198" y="131">4</text><text x="212.5" y="131">5</text><text x="227" y="131">6</text><text x="241.5" y="131">7</text><text x="256" y="131">8</text>
    </g>
    <use href="#foot"/>
  </svg>
</section>

<section class="slide c4 r5">
  <svg viewBox="0 0 277 155">
    <use href="#tab"/>
    <text class="title" x="138.5" y="22" style="fill:#444">Competition Table</text>
    <g class="txc">
      <text x="110" y="43">You can replace</text><text x="110" y="46.5">this text.</text>
      <text x="152" y="43">You can replace</text><text x="152" y="46.5">this text.</text>
      <text x="194" y="43">You can replace</text><text x="194" y="46.5">this text.</text>
      <text x="236" y="43">You can replace</text><text x="236" y="46.5">this text.</text>
    </g>
    <rect x="21" y="55" width="68" height="82" fill="var(--blue)"/>
    <rect x="89" y="55" width="42" height="82" fill="var(--orange)"/>
    <rect x="131" y="55" width="126" height="72" fill="#f4f4f4"/>
    <rect x="89" y="127" width="168" height="10" fill="#bdbdbd"/>
    <g stroke="#fff" stroke-width=".5">
      <line x1="21" y1="67" x2="257" y2="67"/><line x1="21" y1="79" x2="257" y2="79"/><line x1="21" y1="91" x2="257" y2="91"/>
      <line x1="21" y1="103" x2="257" y2="103"/><line x1="21" y1="115" x2="257" y2="115"/><line x1="21" y1="127" x2="257" y2="127"/>
      <line x1="131" y1="55" x2="131" y2="137"/><line x1="173" y1="55" x2="173" y2="137"/><line x1="215" y1="55" x2="215" y2="137"/>
    </g>
    <g class="white" style="font-size:3px">
      <text x="31" y="62">You can replace this text</text><text x="31" y="74">You can replace this text</text>
      <text x="31" y="86">You can replace this text</text><text x="31" y="98">You can replace this text</text>
      <text x="31" y="110">You can replace this text</text><text x="31" y="122">You can replace this text</text>
    </g>
    <g class="white" text-anchor="middle" style="font-size:5px">
      <text x="110" y="62.5">✓</text><text x="110" y="74.5">✓</text><text x="110" y="86.5">✓</text><text x="110" y="98.5">✓</text><text x="110" y="110.5">✓</text>
    </g>
    <g text-anchor="middle" style="font-size:5px;fill:#333">
      <text x="152" y="63">x</text><text x="194" y="63">x</text><text x="236" y="63">x</text>
      <text x="152" y="75">x</text><text x="194" y="75">x</text><text x="236" y="75">x</text>
      <text x="152" y="87">x</text><text x="194" y="87">x</text><text x="236" y="87">x</text>
      <text x="152" y="99">x</text><text x="194" y="99">x</text><text x="236" y="99">x</text>
      <text x="152" y="111">x</text><text x="194" y="111">x</text><text x="236" y="111">x</text>
    </g>
    <use href="#foot"/>
  </svg>
</section>

<!-- Row 6 -->
<section class="slide c1 r6">
  <svg viewBox="0 0 277 155">
    <use href="#tab"/>
    <text class="title" x="138.5" y="22">Business Strategy Diagram</text>
    <g fill="none" stroke-width="11" transform="rotate(-90 108 92)">
      <circle cx="108" cy="92" r="32" stroke="var(--blue)" stroke-dasharray="60 141"/>
      <circle cx="108" cy="92" r="32" stroke="#888" stroke-dasharray="60 141" stroke-dashoffset="-67"/>
      <circle cx="108" cy="92" r="32" stroke="var(--orange)" stroke-dasharray="60 141" stroke-dashoffset="-134"/>
    </g>
    <g fill="none" stroke-width="11" transform="rotate(-90 172 92)">
      <circle cx="172" cy="92" r="32" stroke="var(--orange)" stroke-dasharray="60 141"/>
      <circle cx="172" cy="92" r="32" stroke="var(--blue)" stroke-dasharray="60 141" stroke-dashoffset="-67"/>
      <circle cx="172" cy="92" r="32" stroke="#888" stroke-dasharray="60 141" stroke-dashoffset="-134"/>
    </g>
    <circle cx="108" cy="92" r="13" fill="var(--orange)" stroke="#fff" stroke-width="1.5"/>
    <path d="M104 96v-5M107 96v-7M110 96v-4M113 96v-6" class="ico"/>
    <circle cx="172" cy="92" r="13" fill="var(--blue)" stroke="#fff" stroke-width="1.5"/>
    <circle cx="172" cy="92" r="3.5" class="ico"/>
    <use href="#foot"/>
  </svg>
</section>

<section class="slide c2 r6">
  <svg viewBox="0 0 277 155">
    <use href="#tab"/>
    <text class="title" x="138.5" y="22">Two factors &amp; conclusion</text>
    <text x="18" y="50" class="head">Lorem ipsum dolor</text>
    <use href="#short" x="18" y="55"/>
    <g class="tx"><text x="18" y="70">▸ Lorem ipsum dolor</text><text x="18" y="76">▸ Sit amet consectetur adipiscing</text><text x="18" y="82">▸ Do eiusmod tempor</text><text x="18" y="88">▸ Et pero ipsum do</text><text x="18" y="94">▸ Lorem ipsum dolor</text></g>
    <text x="197" y="50" class="head">Lorem ipsum dolor</text>
    <use href="#short" x="197" y="55"/>
    <g class="tx"><text x="197" y="70">▸ Lorem ipsum dolor</text><text x="197" y="76">▸ Sit amet consectetur adipiscing</text><text x="197" y="82">▸ Do eiusmod tempor</text><text x="197" y="88">▸ Et pero ipsum do</text><text x="197" y="94">▸ Lorem ipsum dolor</text></g>
    <path d="M140 54a26 26 0 0 0 0 52" fill="none" stroke="var(--orange)" stroke-width="13"/>
    <path d="M140 54a26 26 0 0 1 0 52" fill="none" stroke="var(--blue)" stroke-width="13"/>
    <path d="M146 47V112H40L33 119L40 126H146Z" fill="var(--blue)"/>
    <path d="M140 112H240L248 119L240 126H134Z" fill="var(--orange)"/>
    <text x="85" y="121" text-anchor="middle" class="white" style="font-size:4.5px;font-weight:700">Lorem ipsum dolor</text>
    <text x="200" y="121" text-anchor="middle" class="white" style="font-size:4.5px;font-weight:700">Lorem ipsum dolor</text>
    <use href="#foot"/>
  </svg>
</section>

<section class="slide c3 r6">
  <svg viewBox="0 0 277 155">
    <use href="#tab"/>
    <text class="title" x="138.5" y="22">Business Strategy Diagram</text>
    <text x="21" y="47" class="head" style="font-size:4px">Lorem ipsum dolor</text>
    <text x="21" y="53" style="font-size:3px;font-weight:700;fill:#333">Lorem ipsum dolor sit amet, consectetur</text>
    <text x="21" y="57" style="font-size:3px;font-weight:700;fill:#333">adipiscing elit, sed do eiusmod tempor</text>
    <g class="tx" style="fill:var(--blue)">
      <text x="21" y="67">▸ Lorem ipsum dolor</text><text x="21" y="75">▸ Sit amet consectetur adipiscing</text>
      <text x="21" y="83">▸ Do eiusmod tempor</text><text x="21" y="91">▸ Et pero ipsum do</text>
      <text x="21" y="99">▸ Lorem ipsum dolor</text><text x="21" y="107">▸ Do eiusmod tempor</text>
      <text x="21" y="115">▸ Et pero ipsum do</text><text x="21" y="123">▸ Lorem ipsum dolor</text>
    </g>
    <g fill="none" stroke-width="16" transform="rotate(-90 203 93)">
      <circle cx="203" cy="93" r="34" stroke="#555" stroke-dasharray="42.7 171"/>
      <circle cx="203" cy="93" r="34" stroke="var(--blue)" stroke-dasharray="106.8 107" stroke-dashoffset="-42.7"/>
      <circle cx="203" cy="93" r="34" stroke="var(--orange)" stroke-dasharray="21.4 193" stroke-dashoffset="-149.5"/>
      <circle cx="203" cy="93" r="34" stroke="#aaa" stroke-dasharray="43.2 171" stroke-dashoffset="-170.9"/>
    </g>
    <g class="white" style="font-size:3.5px"><text x="214" y="80">2</text><text x="192" y="80">2</text><text x="177" y="95">1</text><text x="211" y="122">5</text></g>
    <g style="font-size:3px;fill:#444">
      <rect x="173" y="137" width="2" height="2" fill="var(--blue)"/><text x="176" y="139">One</text>
      <rect x="186" y="137" width="2" height="2" fill="var(--orange)"/><text x="189" y="139">Two</text>
      <rect x="199" y="137" width="2" height="2" fill="#aaa"/><text x="202" y="139">Three</text>
      <rect x="214" y="137" width="2" height="2" fill="#555"/><text x="217" y="139">Four</text>
    </g>
    <use href="#foot"/>
  </svg>
</section>

<section class="slide c4 r6">
  <svg viewBox="0 0 277 155">
    <use href="#tab"/>
    <text class="title" x="138.5" y="22">Timeline</text>
    <line x1="0" y1="116" x2="277" y2="116" stroke="var(--blue)" stroke-width=".7"/>
    <g stroke="#aaa" stroke-width=".3">
      <line x1="35" y1="52" x2="35" y2="116"/><line x1="86" y1="75" x2="86" y2="116"/>
      <line x1="137" y1="52" x2="137" y2="116"/><line x1="189" y1="75" x2="189" y2="116"/><line x1="240" y1="52" x2="240" y2="116"/>
    </g>
    <g fill="var(--blue)">
      <circle cx="35" cy="52" r="2.5"/><circle cx="86" cy="75" r="2.5"/><circle cx="137" cy="52" r="2.5"/>
      <circle cx="189" cy="75" r="2.5"/><circle cx="240" cy="52" r="2.5"/>
      <circle cx="35" cy="116" r="2.5"/><circle cx="86" cy="116" r="2.5"/><circle cx="137" cy="116" r="2.5"/>
      <circle cx="189" cy="116" r="2.5"/><circle cx="240" cy="116" r="2.5"/>
    </g>
    <g fill="#fff">
      <rect x="25" y="58" width="20" height="12"/><rect x="76" y="81" width="20" height="12"/><rect x="127" y="58" width="20" height="12"/>
      <rect x="179" y="81" width="20" height="12"/><rect x="230" y="58" width="20" height="12"/>
    </g>
    <g class="txc" style="fill:#222">
      <text x="35" y="62" style="font-weight:700">Text Here</text><text x="35" y="67">Easy to change colors,</text><text x="35" y="70">photos and Text.</text>
      <text x="86" y="85" style="font-weight:700">Text Here</text><text x="86" y="90">Easy to change colors,</text><text x="86" y="93">photos and Text.</text>
      <text x="137" y="62" style="font-weight:700">Text Here</text><text x="137" y="67">Easy to change colors,</text><text x="137" y="70">photos and Text.</text>
      <text x="189" y="85" style="font-weight:700">Text Here</text><text x="189" y="90">Easy to change colors,</text><text x="189" y="93">photos and Text.</text>
      <text x="240" y="62" style="font-weight:700">Text Here</text><text x="240" y="67">Easy to change colors,</text><text x="240" y="70">photos and Text.</text>
    </g>
    <rect x="231" y="121" width="18" height="7" fill="var(--orange)"/>
    <g text-anchor="middle" style="font-size:4.5px;font-weight:700;fill:var(--blue)">
      <text x="35" y="126.5">2006</text><text x="86" y="126.5">2010</text><text x="137" y="126.5">2018</text>
      <text x="189" y="126.5">2019</text><text x="240" y="126.5" class="white">2020</text>
    </g>
    <use href="#foot"/>
  </svg>
</section>

<!-- Row 7 -->
<section class="slide b1 r7">
  <svg viewBox="0 0 277 155">
    <use href="#tab"/>
    <text class="title" x="138.5" y="22">Organizational Chart</text>
    <g stroke="#999" stroke-width=".4" fill="none">
      <path d="M138.5 44V50M55 50H222M55 50V55M138.5 50V55M222 50V55"/>
      <path d="M33 67V140M33 83.5H44M33 106.5H44M33 129.5H44"/>
      <path d="M116 67V140M116 83.5H127M116 106.5H127M116 129.5H127"/>
      <path d="M199 67V140M199 83.5H210M199 106.5H210M199 129.5H210"/>
    </g>
    <rect x="109" y="32" width="59" height="6" fill="var(--blue)"/><rect x="109" y="38" width="59" height="6" fill="var(--orange)"/>
    <rect x="26" y="55" width="58" height="6" fill="var(--orange)"/><rect x="26" y="61" width="58" height="6" fill="#555"/>
    <rect x="109" y="55" width="58" height="6" fill="var(--orange)"/><rect x="109" y="61" width="58" height="6" fill="#555"/>
    <rect x="192" y="55" width="58" height="6" fill="var(--orange)"/><rect x="192" y="61" width="58" height="6" fill="#555"/>
    <g fill="#ededed">
      <rect x="44" y="78" width="40" height="11"/><rect x="44" y="101" width="40" height="11"/><rect x="44" y="124" width="40" height="11"/>
      <rect x="127" y="78" width="40" height="11"/><rect x="127" y="101" width="40" height="11"/><rect x="127" y="124" width="40" height="11"/>
      <rect x="210" y="78" width="40" height="11"/><rect x="210" y="101" width="40" height="11"/><rect x="210" y="124" width="40" height="11"/>
    </g>
    <g class="white" text-anchor="middle" style="font-size:2.6px">
      <text x="138.5" y="36">FIRST / LAST NAME</text><text x="138.5" y="42">Position</text>
      <text x="55" y="59">FIRST / LAST NAME</text><text x="55" y="65">Position</text>
      <text x="138" y="59">FIRST / LAST NAME</text><text x="138" y="65">Position</text>
      <text x="221" y="59">FIRST / LAST NAME</text><text x="221" y="65">Position</text>
    </g>
    <g class="txc" style="fill:#999">
      <text x="64" y="83">FIRST / LAST NAME</text><text x="64" y="87">Position</text>
      <text x="64" y="106">FIRST / LAST NAME</text><text x="64" y="110">Position</text>
      <text x="64" y="129">FIRST / LAST NAME</text><text x="64" y="133">Position</text>
      <text x="147" y="83">FIRST / LAST NAME</text><text x="147" y="87">Position</text>
      <text x="147" y="106">FIRST / LAST NAME</text><text x="147" y="110">Position</text>
      <text x="147" y="129">FIRST / LAST NAME</text><text x="147" y="133">Position</text>
      <text x="230" y="83">FIRST / LAST NAME</text><text x="230" y="87">Position</text>
      <text x="230" y="106">FIRST / LAST NAME</text><text x="230" y="110">Position</text>
      <text x="230" y="129">FIRST / LAST NAME</text><text x="230" y="133">Position</text>
    </g>
    <use href="#foot"/>
  </svg>
</section>

<section class="slide b2 r7">
  <svg viewBox="0 0 277 155">
    <polygon points="41,0 122,0 96,155 14,155" fill="var(--blue)"/>
    <g class="white" text-anchor="middle" style="font-size:11.5px;font-weight:700">
      <text x="68" y="67">Clients</text><text x="68" y="82">We Work</text><text x="68" y="97">With</text>
    </g>
    <g fill="#f1f1f1" stroke="#e3e3e3" stroke-width=".4">
      <rect x="128" y="28" width="63" height="29"/><rect x="202" y="28" width="63" height="29"/>
      <rect x="128" y="64" width="63" height="29"/><rect x="202" y="64" width="63" height="29"/>
      <rect x="128" y="100" width="63" height="29"/><rect x="202" y="100" width="63" height="29"/>
    </g>
    <g text-anchor="middle" style="font-size:6.5px;font-weight:500;fill:#8a8a8a">
      <text x="159.5" y="39" style="font-size:5px">Name or</text><text x="159.5" y="47">LOGO</text>
      <text x="233.5" y="45">Vexmora</text>
      <text x="159.5" y="81">Tandrel</text>
      <text x="233.5" y="81">Olvique</text>
      <text x="159.5" y="117">Pellaro</text>
      <text x="233.5" y="117">Kestrune</text>
    </g>
  </svg>
</section>

<section class="slide b3 r7">
  <svg viewBox="0 0 277 155">
    <text class="wordmark" x="138.5" y="34" style="font-size:25px">FE·N·DRA</text>
    <text class="tagline" x="138.5" y="46" style="font-size:6px">SIMPLY FENDRA</text>
    <rect x="82" y="58" width="114" height="16" fill="var(--orange)"/>
    <text x="139" y="68.5" text-anchor="middle" class="white" style="font-size:7.5px;font-weight:700">Contact with Us</text>
    <text x="138.5" y="89" class="txc">Lorem ipsum dolor sit amet, consectetur adipiscing elit, sed do eiusmod tempor incididunt ut labore</text>
    <text x="138.5" y="93" class="txc">et dolore magna aliqua</text>
    <line x1="90" y1="102" x2="188" y2="102" stroke="#ddd" stroke-width=".4"/>
    <g fill="#fff" stroke="var(--blue)" stroke-width=".8">
      <circle cx="94" cy="124" r="9"/><circle cx="117" cy="124" r="9"/><circle cx="140" cy="124" r="9"/>
      <circle cx="163" cy="124" r="9"/><circle cx="186" cy="124" r="9"/>
    </g>
    <g fill="none" stroke="var(--blue)" stroke-width=".9" stroke-linecap="round" stroke-linejoin="round">
      <path d="M90.5 119.5c0 5 3 8.5 8 9l1.2-2-2.3-1.3-1.1 1c-1.4-.6-2.6-2-3.3-3.4l1-1.1-1.2-2.4z"/>
      <rect x="112.5" y="121" width="9" height="6.5" rx=".8"/><path d="M112.5 121.5l4.5 3.3 4.5-3.3"/>
      <path d="M140 129.5s-3.5-3.8-3.5-6.5a3.5 3.5 0 0 1 7 0c0 2.7-3.5 6.5-3.5 6.5z"/><circle cx="140" cy="123" r="1.2"/>
      <circle cx="163" cy="124" r="4.5"/><path d="M158.5 124h9M163 119.5c-2.5 3-2.5 6 0 9M163 119.5c2.5 3 2.5 6 0 9"/>
    </g>
  </svg>
</section>

</body>
</html>
```